Corporate Branding - Web and Print

A UK based company will like to use an existing logo to create branding materials for all marketing related documents, including business card, prints, letterhead, Website, Twitter, Facebook, Instagram logo etc. This company serves high-end clientele in the fashion, health and wellness and as such high quality and class is of utmost importance.
Where the logo can be modernised without losing its character then experiment. The main thing is to have a corporate branding which can be used later for brochures, Business Plan infographics.
The prominent colour within the organisation is burnt orange with no secondary colour. However if you believe a secondary colour is needed then use it, otherwise keep it simple and classy. Any chosen colours have to match perfectly.
Target Market(s)
High net worth individuals
Industry/Entity Type
Health And Wellness
Contact Information for Business Card
classy
Look and feel
Each slider illustrates characteristics of the customer's brand and the style your logo design should communicate.

```html
<!DOCTYPE html>
<html lang="en">
<head>
<meta charset="utf-8">
<title>Velora Business Card</title>
<link rel="stylesheet" href="https://fonts.googleapis.com/css2?family=Roboto:wght@400;500;700&display=swap">
<style>
  :root {
    --burnt-orange: #f4921f;
    --orange-light: #f7a640;
    --card-white: #f6f6f6;
    --backdrop: #e4e4e4;
    --text-white: #ffffff;
  }
  * { margin: 0; padding: 0; box-sizing: border-box; }
  html, body {
    width: 1200px; height: 886px; overflow: hidden;
    background: var(--backdrop);
    font-family: "Roboto", Arial, sans-serif;
  }
  .canvas {
    width: 1200px; height: 886px;
    display: flex; flex-direction: column; align-items: center; justify-content: center;
    gap: 56px;
  }
  .card {
    position: relative;
    width: 600px; height: 343px;
    border-radius: 20px;
    overflow: hidden;
    box-shadow: 0 6px 18px rgba(0,0,0,0.18);
  }
  .card-back {
    background: linear-gradient(135deg, var(--orange-light), var(--burnt-orange) 60%);
  }
  .back-brand {
    position: absolute; right: 44px; bottom: 96px;
    text-align: left;
  }
  .back-brand .brand-name {
    font-weight: 700; font-size: 40px; letter-spacing: 2px;
    color: var(--text-white); line-height: 1;
  }
  .back-brand .brand-web {
    margin-top: 6px;
    font-size: 13px; letter-spacing: 7px; color: var(--text-white);
  }
  .card-front { background: var(--card-white); }
  .front-shape { position: absolute; inset: 0; }
  .front-brand {
    position: absolute; left: 120px; top: 74px;
    display: flex; flex-direction: column; align-items: center; gap: 10px;
  }
  .front-brand .brand-dot {
    width: 42px; height: 42px; border-radius: 50%;
    background: var(--burnt-orange);
  }
  .front-brand .brand-name {
    font-weight: 700; font-size: 38px; letter-spacing: 2px;
    color: var(--burnt-orange); line-height: 1;
  }
  .holder {
    position: absolute; right: 34px; top: 58px;
    text-align: right; color: var(--text-white);
  }
  .holder .name { font-weight: 700; font-size: 20px; }
  .holder .title { font-weight: 500; font-size: 14px; margin-top: 2px; }
  .contact {
    position: absolute; right: 34px; top: 176px;
    text-align: right; color: var(--text-white);
    font-size: 14px; line-height: 19px;
  }
  .contact .address { margin-bottom: 6px; }
  .contact .line { display: flex; justify-content: flex-end; align-items: center; gap: 8px; }
  .contact svg { width: 13px; height: 13px; fill: var(--text-white); flex: none; }
</style>
</head>
<body>
<main class="canvas">
  <section class="card card-back">
    <div class="back-brand">
      <div class="brand-name">VELORA</div>
      <div class="brand-web">www.velora.com</div>
    </div>
  </section>

  <section class="card card-front">
    <svg class="front-shape" viewBox="0 0 600 343" preserveAspectRatio="none">
      <defs>
        <linearGradient id="frontOrange" x1="0" y1="0" x2="1" y2="0">
          <stop offset="0" stop-color="#f7a640"/>
          <stop offset="0.4" stop-color="#f4921f"/>
        </linearGradient>
      </defs>
      <path d="M360,0 C330,170 250,290 130,343 L600,343 L600,0 Z" fill="url(#frontOrange)"/>
      <path d="M372,18 C330,170 240,265 120,310 C250,275 345,180 372,18 Z" fill="var(--burnt-orange)"/>
    </svg>

    <div class="front-brand">
      <div class="brand-dot"></div>
      <div class="brand-name">VELORA</div>
    </div>

    <div class="holder">
      <div class="name">DANIEL HART</div>
      <div class="title">CEO/FOUNDER</div>
    </div>

    <div class="contact">
      <div class="address">412 Willow Court<br>Bristol, Avon 20318</div>
      <div class="line">201 555 0148
        <svg viewBox="0 0 16 16"><path d="M3 1l3 3-2 2c1 2 3 4 5 5l2-2 3 3-2 3C7 15 1 9 0 3z"/></svg></div>
      <div class="line">201 555 0172
        <svg viewBox="0 0 16 16"><path d="M4 0h8v16H4zM5.5 2v10h5V2zM7 13.5h2v1H7z" fill-rule="evenodd"/></svg></div>
      <div class="line">201 555 0196
        <svg viewBox="0 0 16 16"><path d="M4 1h8v4H4zM1 6h14v7h-3v2H4v-2H1zM5 10v4h6v-4z" fill-rule="evenodd"/></svg></div>
      <div class="line">daniel@velora.com
        <svg viewBox="0 0 16 16"><path d="M0 3h16v10H0zM1.5 4.5L8 9l6.5-4.5z" fill-rule="evenodd"/></svg></div>
      <div class="line">www.velora.com
        <svg viewBox="0 0 16 16"><circle cx="8" cy="8" r="7.5"/></svg></div>
    </div>
  </section>
</main>
</body>
</html>
```